Electrical Wholesaler Needs a New Website

Looking for a new website to be built for an electrical wholesaler based in Birmingham(England). Our logo is based on two Lions with a shield, so ideally the site should be deigned around that.

Looking for something that shows off our logo and incorporates what we are trying to do, preferably to have a colour scheme that is green and black if possible.

Target Market(s)

I'm looking for a professional website for my company that doesn't just look like amother WordPress template that I could build myself.

Industry/Entity Type

Electrical

Font styles to use
Sans Serif

Colors
9bcb3c
cadf82

Requirements
Must have
• Website with 4-5 pages, home page, about us, suppliers list, catalogue download and contact us. Search for UK electrical wholesalers to give you an idea of what I mean.

```html
<!DOCTYPE html>
<html lang="en">
<head>
<meta charset="utf-8">
<title>Ridgeway Electrical Wholesalers</title>
<link rel="stylesheet" href="https://fonts.googleapis.com/css2?family=Questrial&family=Open+Sans:wght@400;600;700&family=Teko:wght@500;600&display=swap">
<style>
:root{
  --lime:#8dc63f;
  --lime-dark:#6fa52b;
  --forest:#1f5e33;
  --forest-deep:#14462a;
  --olive:#7a9a22;
  --ink:#111;
  --text:#444;
  --panel:#1b1d1b;
  --frame:#4e8f3a;
}
*{margin:0;padding:0;box-sizing:border-box}
html,body{width:1200px;height:1184px;overflow:hidden;background:#fff}
body{position:relative;font-family:'Questrial',sans-serif;color:var(--text)}
.abs{position:absolute}
.top-line{left:0;top:0;width:1200px;height:2px;background:var(--lime)}
.brand{left:200px;top:44px}
.brand-mark{display:inline-block;width:12px;height:12px;background:var(--forest);margin-right:6px;vertical-align:middle}
.brand-name{font-family:'Open Sans',sans-serif;font-weight:700;font-size:30px;color:var(--forest);vertical-align:middle;letter-spacing:.5px}
.brand-sub{font-size:8px;color:var(--forest);margin-top:2px;letter-spacing:.3px}
.phone{left:816px;top:0;width:185px;height:33px;background:var(--forest-deep);border-bottom:3px solid var(--lime);color:#fff;font-family:'Open Sans',sans-serif;font-style:italic;font-weight:600;font-size:21px;display:flex;align-items:center;justify-content:center;gap:6px}
.nav-band{left:0;top:110px;width:1200px;height:38px;background:var(--lime);border-bottom:3px solid var(--lime-dark)}
.nav{left:199px;top:110px;height:36px;display:flex;list-style:none;font-family:'Open Sans',sans-serif;font-size:12px;color:#fff}
.nav li{padding:0 10px;line-height:36px}
.nav li.current{background:var(--ink)}
.nav li+li{margin-left:1px}
.van{left:760px;top:45px;width:240px;height:130px;border-radius:20px 30px 10px 10px;background:linear-gradient(180deg,#f4f4f4,#cfd2cf 70%,#3a3a3a)}
.slider{left:199px;top:176px;width:802px;height:177px;border:3px solid var(--frame);background:#fff;overflow:hidden}
.slider svg{position:absolute;left:0;top:0}
.boxes{left:18px;top:30px;width:300px;height:130px;background:linear-gradient(160deg,#d9b883,#b48a55);border-radius:4px}
.slide-emblem{left:720px;top:30px;width:72px;height:130px;background:radial-gradient(circle,#3f8a2f,#1a1f1a 70%)}
.slide-title{left:404px;top:16px;font-family:'Teko',sans-serif;font-weight:600;font-size:35px;line-height:1;color:var(--lime);white-space:nowrap}
.slide-text{left:406px;top:50px;width:280px;font-family:'Open Sans',sans-serif;font-size:13.5px;line-height:15px;color:#fff}
.slide-btn{left:517px;top:104px;width:113px;height:26px;background:var(--lime);color:#fff;font-family:'Open Sans',sans-serif;font-size:14px;line-height:26px;text-align:center;border-bottom:2px solid var(--lime-dark)}
.dots{left:572px;top:361px;display:flex;gap:5px}
.dots span{width:8px;height:8px;background:var(--frame)}
.dots span:first-child{background:var(--ink)}
.rule{left:199px;width:802px;height:1px;background:#e8eed8}
.welcome{left:201px;top:392px;font-size:27px;color:var(--ink);white-space:nowrap}
.welcome em{font-style:normal;color:var(--olive)}
.intro{left:201px;top:434px;width:780px;font-size:11.4px;line-height:15.5px;color:var(--text)}
.intro p+p{margin-top:15px}
.feature{top:568px;height:120px;border:3px solid var(--frame);overflow:hidden}
.feature .photo{height:95px}
.feature .cap{position:absolute;left:0;right:0;bottom:0;height:22px;background:rgba(255,255,255,.85);color:var(--forest-deep);font-family:'Open Sans',sans-serif;font-weight:600;font-size:12px;letter-spacing:-.3px;text-align:center;line-height:22px;white-space:nowrap}
.catalog-title{left:199px;top:726px;font-size:26px;color:var(--olive)}
.catalog-text{left:200px;top:775px;width:580px;font-size:11.6px;line-height:15.5px}
.catalog-box{left:796px;top:730px;width:205px;height:110px;border:2px solid #ddd;background:#fff}
.catalog-box div{margin:10px 18px;height:86px;background:linear-gradient(120deg,#e9f3d2,#9bcb3c 60%,#2b2b2b)}
.services{left:199px;top:872px;width:541px;height:163px;background:linear-gradient(180deg,#9bcb3c,#6cab2b);border:2px solid #b6d97a;padding:4px;display:grid;grid-template-columns:1fr 1fr;grid-template-rows:1fr 1fr;gap:4px}
.service{border:1px dashed rgba(255,255,255,.55);display:flex;gap:12px;padding:8px 10px;overflow:hidden}
.service .thumb{flex:none;width:70px;height:56px;border:1px solid #fff;background:linear-gradient(135deg,#ddd,#b44 60%,#777)}
.service .thumb.alt{background:linear-gradient(135deg,#888,#cfd6c6 60%,#3a5a2a)}
.service h3{font-family:'Open Sans',sans-serif;font-weight:600;font-size:11.5px;color:var(--ink);letter-spacing:.5px;white-space:nowrap}
.service p{font-family:'Open Sans',sans-serif;font-size:9px;line-height:13px;color:#fff;margin-top:2px}
.links{left:746px;top:872px;width:255px;height:163px;background:var(--panel)}
.links h2{margin:4px 4px 0;height:36px;background:var(--forest-deep);border-bottom:3px solid var(--lime);color:#fff;font-family:'Open Sans',sans-serif;font-weight:700;font-size:20px;text-align:center;line-height:36px}
.links ul{list-style:none;display:grid;grid-template-columns:138px 1fr;row-gap:5px;padding:14px 0 0 10px;font-family:'Open Sans',sans-serif;font-size:11px;color:#eee}
.partners{left:199px;top:1070px;width:802px;display:flex;justify-content:space-between;align-items:center;font-family:'Open Sans',sans-serif;font-weight:700;font-size:20px;color:#1d4f9a}
.partners span{width:122px;text-align:center;white-space:nowrap}
.footer{left:0;top:1135px;width:1200px;height:49px;background:#0d0d0d;color:#eee;font-family:'Open Sans',sans-serif;font-size:11px;text-align:center;line-height:49px}
</style>
</head>
<body>
<div class="abs top-line"></div>

<div class="abs brand">
  <span class="brand-mark"></span><span class="brand-name">Ridgeway</span>
  <div class="brand-sub">ELECTRICAL WHOLESALERS</div>
</div>

<div class="abs phone">
  <svg width="16" height="14" viewBox="0 0 16 14" aria-hidden="true"><path d="M1 4 Q8 -1 15 4 L13 6 L11 4 L5 4 L3 6 Z M4 7 H12 L14 13 H2 Z" fill="#8aa"/></svg>
  0800-555-019
</div>

<div class="abs nav-band"></div>
<ul class="abs nav">
  <li class="current">HOME</li>
  <li>ABOUT US</li>
  <li>SUPPLIERS LIST</li>
  <li>CATALOGUE DOWNLOAD</li>
  <li>CONTACT US</li>
</ul>

<div class="abs van" role="img" aria-label="White delivery van with company livery"></div>

<section class="abs slider">
  <svg width="796" height="171" viewBox="0 0 796 171" aria-hidden="true">
    <path d="M110 0 C270 0 330 30 500 171 L796 171 L796 0 Z" fill="var(--panel)"/>
    <path d="M110 0 C270 0 330 30 500 171" fill="none" stroke="var(--frame)" stroke-width="3"/>
  </svg>
  <div class="abs boxes" role="img" aria-label="Stack of branded cardboard boxes"></div>
  <div class="abs slide-emblem" role="img" aria-label="Green decorative emblem illustration"></div>
  <div class="abs slide-title">IN DEPTH LOCAL STOCKS</div>
  <p class="abs slide-text">Free Delivery on our own vehicles (with no minimum order Charge) on all stock within our delivery aera.</p>
  <div class="abs slide-btn">READMORE&gt;&gt;</div>
</section>

<div class="abs dots"><span></span><span></span><span></span><span></span></div>
<div class="abs rule" style="top:379px"></div>

<h1 class="abs welcome">Welcome To The <em>Ridgeway Electrical Wholesale</em> Website.</h1>
<div class="abs intro">
  <p>We are an independent electrical wholesale distributor with 59 strategically located branches across the UK<br>Our stock of standard products is in excess of £13m and covers electrical installation materials, lamps and lighting fittings, motor control gear, switch and distribution, water heating, space heating and ventilation equipment.</p>
  <p>Each of our branches offers a full trade counter, telephone and delivery service.</p>
  <p>As well as standard products we offer a recycling service and a free in house Lighting Design facility.</p>
</div>

<div class="abs feature" style="left:199px;width:368px">
  <div class="photo" role="img" aria-label="Warehouse building with car park" style="background:linear-gradient(180deg,#dfe6ee,#5b6f94 45%,#8a8a8a)"></div>
  <div class="cap">Quis Nostrud Exerci Tation Ullamcorper Suscipit</div>
</div>
<div class="abs feature" style="left:573px;width:216px">
  <div class="photo" role="img" aria-label="Cable drums on red racking" style="background:linear-gradient(90deg,#8a2a20,#333 40%,#c9a27a)"></div>
  <div class="cap">Ut Wisi Enim Ad Minim Veniam</div>
</div>
<div class="abs feature" style="left:796px;width:205px">
  <div class="photo" role="img" aria-label="Branded delivery lorry on the road" style="background:linear-gradient(180deg,#6f8a5f,#f2f2f2 45%,#555)"></div>
  <div class="cap">Ut Wisi Enim Ad Minim Veniam</div>
</div>

<div class="abs rule" style="top:719px"></div>

<h2 class="abs catalog-title">Check Out Our Catalog</h2>
<p class="abs catalog-text">Customers include electrical contractors, manufacturing industry, local and national goverment organisations, public bodies, utilities, leisure clubs, garden centres, retirement homes - infact anyone with a need for electrical products.</p>
<div class="abs catalog-box"><div role="img" aria-label="Open product catalogue brochure"></div></div>

<section class="abs services">
  <div class="service"><div class="thumb" role="img" aria-label="Lighting product photo"></div><div><h3>Lighting Design Service</h3><p>LDS is a fully comprehensive and free of charge Lighting Design Service provided by qualified light..</p></div></div>
  <div class="service"><div class="thumb" role="img" aria-label="Special product photo"></div><div><h3>Special Product Division</h3><p>Lorem ipsum dolor sit amet, consectetuer adipiscing elit, diam nonummy nibh smod tincidunt ut...</p></div></div>
  <div class="service"><div class="thumb alt" role="img" aria-label="Industrial workshop photo"></div><div><h3>Ridgeway Industrial</h3><p>Established in 1970 Kestrel Air Equipment is a sister company to Ridgeway Electrical ....</p></div></div>
  <div class="service"><div class="thumb alt" role="img" aria-label="Technology products photo"></div><div><h3>New Technology</h3><p>Contact your local branch for details of the latest NEW technology products.</p></div></div>
</section>

<section class="abs links">
  <h2>USEFULL LINKS</h2>
  <ul>
    <li>Technical Information</li><li>Useful Documents</li>
    <li>Terms &amp; Conditions</li><li>WEEE Directive</li>
    <li>Policies</li>
  </ul>
</section>

<div class="abs partners">
  <span>Norvel</span><span>Brackton</span><span>Veldmark</span><span>Airdale</span><span>Lumora</span><span>Hotwell</span>
</div>

<footer class="abs footer">© 2013 RidgewayElectrical.example</footer>
</body>
</html>
```